logo & Business Card Design

BrightHaven Termite & Pest Control, I need a great logo, take my ideas and run with them!
I will use this in marketing and website so needs to be eye catching but professional

Target Market(s)

Resedintial & Business

Industry/Entity Type

Marketing

Contact Information for Business Card

Need front side with pertinent info & Logo; back side will have a 25% off initial services Coupon!

Font styles to use
Sans Serif

Colors
ec1f27
1b1b1b

Requirements
Must have
• Professional logo and style
Nice to have
• Raised lettering, black, red, white colors maybe? I'm flexible, but those colors go good on any background, vehicle, uniform, etc...
Should not have
• Cheesy

```html
<!DOCTYPE html>
<html lang="en">
<head>
<meta charset="UTF-8">
<title>BrightHaven Termite &amp; Pest Control – Business Card</title>
<link href="https://fonts.googleapis.com/css2?family=Lato:wght@300;400;700;900&display=swap" rel="stylesheet">
<style>
  :root {
    --stage: #ebe8e4;
    --card-white: #ffffff;
    --card-dark: #2a2a2a;
    --accent: #e8562a;
    --ink: #5a5a5a;
    --ink-soft: #8a8a8a;
    --rule-light: #d9d9d9;
    --rule-dark: #3d3d3d;
    --band-edge: #4a4a4a;
    --text-on-dark: #9a9a9a;
    --text-bright: #ffffff;
  }
  * { margin: 0; padding: 0; box-sizing: border-box; }
  html, body {
    width: 1200px; height: 788px; overflow: hidden;
    background: var(--stage);
    font-family: "Lato", Arial, sans-serif;
  }
  .stage {
    position: relative; width: 1200px; height: 788px;
    display: flex; align-items: center; justify-content: center; gap: 50px;
  }
  .card {
    position: relative; width: 525px; height: 300px;
    box-shadow: 0 10px 28px rgba(0,0,0,0.18);
    overflow: hidden;
  }

  /* Front card */
  .card--front { background: var(--card-white); }
  .brand { position: absolute; text-align: left; }
  .card--front .brand { top: 28px; right: 34px; }
  .brand__name {
    font-weight: 700; font-size: 30px; letter-spacing: 0.5px;
    line-height: 1; text-transform: uppercase;
  }
  .card--front .brand__name { color: var(--accent); }
  .brand__sub { font-weight: 400; font-size: 14px; color: var(--ink-soft); margin-top: 3px; }
  .card--front .brand__tagline { font-size: 9.5px; color: var(--ink); margin-top: 4px; }

  .person { position: absolute; left: 34px; top: 140px; width: 240px; }
  .person__name {
    font-weight: 700; font-size: 21px; text-transform: uppercase;
    color: var(--ink); letter-spacing: 0.3px;
  }
  .person__name .first { color: var(--accent); }
  .person__title {
    font-size: 10.5px; letter-spacing: 1px; color: var(--ink-soft);
    text-transform: uppercase; padding-bottom: 9px;
    border-bottom: 1px solid var(--rule-light);
  }
  .contacts { list-style: none; margin-top: 14px; }
  .contacts li {
    display: flex; align-items: center; gap: 14px;
    font-size: 11.5px; color: var(--ink); margin-bottom: 9px;
  }
  .contacts svg { width: 12px; height: 12px; fill: none; stroke: var(--accent); stroke-width: 1.6; }

  .band {
    position: absolute; left: 0; right: 0; bottom: 0; height: 16px;
    background: var(--accent); border-top: 3px solid var(--band-edge);
    display: flex; align-items: center; justify-content: flex-end;
    padding-right: 20px;
  }
  .band__web { font-size: 9px; color: var(--text-bright); letter-spacing: 0.3px; }

  /* Back card */
  .card--back { background: linear-gradient(160deg, #303030, var(--card-dark) 60%, #242424); }
  .card--back .brand { top: 108px; left: 50%; transform: translateX(-50%); }
  .card--back .brand__name { color: var(--text-bright); font-size: 34px; }
  .card--back .brand__sub { color: var(--text-on-dark); font-size: 15px; margin-top: 4px; }
  .back-tagline {
    position: absolute; left: 40px; right: 40px; bottom: 40px;
    display: flex; align-items: center; gap: 10px;
    font-size: 10px; color: var(--text-on-dark); white-space: nowrap;
  }
  .back-tagline::before, .back-tagline::after {
    content: ""; flex: 1; height: 1px; background: var(--rule-dark);
  }
  .back-edge {
    position: absolute; left: 0; right: 0; bottom: 16px; height: 1px;
    background: var(--rule-dark);
  }
</style>
</head>
<body>
<main class="stage">
  <section class="card card--front" aria-label="Business card front">
    <div class="brand">
      <div class="brand__name">BrightHaven</div>
      <div class="brand__sub">Termite &amp; Pest Control</div>
      <div class="brand__tagline">Lasting Protection for Your Home or Business</div>
    </div>
    <div class="person">
      <h1 class="person__name"><span class="first">Daniel</span> K. Mercer</h1>
      <p class="person__title">Project Manager</p>
      <ul class="contacts">
        <li>
          <svg viewBox="0 0 12 12" aria-hidden="true"><rect x="3" y="1" width="6" height="10" rx="1"/><line x1="5" y1="9" x2="7" y2="9"/></svg>
          +000 - 5550 - 1824
        </li>
        <li>
          <svg viewBox="0 0 12 12" aria-hidden="true"><path d="M2 4 Q6 1 10 4 L9 5.5 L7.5 4.5 L4.5 4.5 L3 5.5 Z"/><rect x="2.5" y="6" width="7" height="4.5" rx="0.8"/></svg>
          +000 - 5550 - 2290
        </li>
        <li>
          <svg viewBox="0 0 12 12" aria-hidden="true"><rect x="1" y="2.5" width="10" height="7" rx="0.8"/><path d="M1 3 L6 7 L11 3"/></svg>
          daniel@brighthavenpest.com
        </li>
      </ul>
    </div>
    <div class="band"><span class="band__web">www.brighthavenpest.com</span></div>
  </section>

  <section class="card card--back" aria-label="Business card back">
    <div class="brand">
      <div class="brand__name">BrightHaven</div>
      <div class="brand__sub">Termite &amp; Pest Control</div>
    </div>
    <p class="back-tagline">Lasting Protection for Your Home or Business</p>
    <div class="back-edge"></div>
  </section>
</main>
</body>
</html>
```